依頼概要
■依頼の目的/概要
夢をかなえる人だけが気づいている「月の舟の旅」の秘密の味わい方のデザインをお願いします。

■本の内容
詳しくは添付ファイルを読んでいただいてデザインをお願いします。
シンデレラ物語は実は現実の物語で、成功に導く内容が含まれているものだったという内容になります。

■デザイン要望
明るいもの、好印象が持てるようなものがいいかと思っています。
その他何かご不明な点がございましたら、お気軽にご質問下さい。
よろしくお願いいたします。
夢をかなえる人だけが気づいている「月の舟の旅」の秘密の味わい方
は電子書籍です。
著者名は タケル K  です。
ご提案誠にありがとうございます。

デザイン上支障がない場合には

読者様限定

シンデレラ度チェックシート

プレゼント

などの文言を入れてみてもらってもよいでしょうか?
■ 選んだ理由

数多くの素敵な提案ありがとうございました。
私だけでは決めかねて迷うほどでしたので、知人、電子書籍出版グループのメンバーに意見(投票)を伺いながら決定しました。
その際
〇シンデレラの世界観に沿ったデザインの雰囲気、わかりやすさ
〇中央下のガラスの靴のインパクト
〇文中からの言葉
などが高評価となっていましたので、決めさせていただきました。

■ 提案者全員のお礼・コメント

この度は、数多くの素敵な提案をいただき誠にありがとうございました。
感謝いたしております。
皆様方の今後のご活躍を願っております。
またご縁がございましたら、その節はよろしくお願い申し上げます。

```html
<!DOCTYPE html>
<html lang="ja">
<head>
<meta charset="utf-8">
<title>夢をかなえる人だけが気づいている「月の舟の旅」の秘密の味わい方</title>
<link rel="stylesheet" href="https://fonts.googleapis.com/css2?family=Noto+Serif+JP:wght@700;900&family=Noto+Sans+JP:wght@700&family=Great+Vibes&display=swap">
<style>
:root{
  --frame:#8fd3e6;
  --frame-edge:#6cc3dc;
  --stripe:#e2f3f9;
  --paper:#ffffff;
  --ink:#3c4756;
  --gem-area:#a9def0;
  --ornament:#d4dbe1;
  --glass:#c6e8f2;
  --glass-light:#e6f6fb;
}
*{margin:0;padding:0;box-sizing:border-box}
html,body{width:896px;height:1200px;overflow:hidden;background:var(--paper)}
.cover{position:relative;width:896px;height:1200px;background:var(--frame);border:2px solid var(--frame-edge)}
.cover-panel{position:absolute;left:56px;top:56px;right:56px;bottom:56px;
  background:repeating-linear-gradient(90deg,var(--paper) 0 42px,var(--stripe) 42px 84px);}
.gem-area{position:absolute;width:84px;height:84px;background:var(--gem-area)}
.gem-tl{left:14px;top:14px}.gem-tr{right:14px;top:14px}
.gem-bl{left:14px;bottom:14px}.gem-br{right:14px;bottom:14px}
.tiara{position:absolute;left:368px;top:76px;width:160px;height:60px;background:var(--ornament)}
.slipper{position:absolute;left:70px;top:950px;width:400px;height:150px;
  background:linear-gradient(180deg,var(--glass-light),var(--glass))}
.vert{position:absolute;writing-mode:vertical-rl;white-space:nowrap;color:var(--ink)}
.title-lead{left:600px;top:170px;font-family:"Noto Sans JP",sans-serif;font-weight:700;font-size:42px;letter-spacing:2px}
.title-main{left:452px;top:160px;font-family:"Noto Serif JP",serif;font-weight:900;font-size:84px;line-height:1}
.title-sub{left:336px;top:300px;font-family:"Noto Serif JP",serif;font-weight:900;font-size:84px;line-height:1}
.author{left:236px;top:420px;font-family:"Noto Serif JP",serif;font-weight:700;font-size:36px;letter-spacing:4px}
.tagline{left:150px;top:260px;font-family:"Great Vibes",cursive;font-size:30px;line-height:1.3;color:var(--ink);text-orientation:sideways}
</style>
</head>
<body>
<main class="cover">
  <div class="cover-panel"></div>
  <div class="gem-area gem-tl" role="img" aria-label="Blue jewel ornament"></div>
  <div class="gem-area gem-tr" role="img" aria-label="Blue jewel ornament"></div>
  <div class="gem-area gem-bl" role="img" aria-label="Blue jewel ornament"></div>
  <div class="gem-area gem-br" role="img" aria-label="Blue jewel ornament"></div>
  <div class="tiara" role="img" aria-label="Silver tiara ornament"></div>
  <div class="slipper" role="img" aria-label="Glass slipper illustration"></div>

  <h1>
    <span class="vert title-lead">夢をかなえる人だけが気づいている</span>
    <span class="vert title-main">「月の舟の旅」の</span>
    <span class="vert title-sub">秘密の味わい方</span>
  </h1>
  <p class="vert author">タケル K 著</p>
  <p class="vert tagline">Story of "Moon Boat"<br>True dream story</p>
</main>
</body>
</html>
```